Ferncastle Holdings - stationery for luxury, exclusive property investment company

We need stationery (letterhead, folder, compliments slip and envelope) and business cards which will reflect our luxury brand.

I have attached some design examples that we like.

We are an investment company which buys property to provide accommodation for corporate customers.

The design of the stationery needs to be be simple, refined, understated, luxury and very tasteful.

The design should communicate luxury and exclusivity, without being ostentatious.

Logo files are attached

Please can designers re-read the brief, and make sure the logo is in gold on either on a navy or white background.

Target Market(s)

Wealthy customers

Contact Information for Business Card

Helen Travers-Booth
Director
Ferncastle Holdings Limited
email: helen@ferncastleholdings.co.uk
mob: 07712645930

Font styles to use
Serif

Colors

Designer to choose colors to be used in the design.

Requirements
Must have
• The logo must be gold on either a white or navy background as per the attached logos.
• The stationery MUST have the following information:
• Ferncastle Holdings Limited
• The Willows
• Ashby Rise
• Ashby
• GL52 7TN
• Company Number: 20418736 (Registered in England and Wales)
• The letterhead must also have the two attached logos for the PLG and the PLG accreditation scheme. They do not need to be large.
Nice to have
• A watermark, navy banding either top or bottom.
Should not have
• Anything that looks budget.

```html
<!DOCTYPE html>
<html lang="en">
<head>
<meta charset="utf-8">
<title>Ferncastle Holdings – Business Card</title>
<link rel="stylesheet" href="https://fonts.googleapis.com/css2?family=Cinzel:wght@500&family=Barlow+Condensed:ital,wght@0,300;0,500;0,600;1,300&display=swap">
<style>
  :root {
    --navy: #1d1b48;
    --navy-deep: #161438;
    --gold: #c79f52;
    --paper: #f7f7f5;
    --stage: #ffffff;
    --label-grey: #9a9aa3;
    --ink: #1a1840;
    --band-text: #c9c9d6;
  }
  * { box-sizing: border-box; margin: 0; padding: 0; }
  html, body {
    width: 1200px; height: 1000px; overflow: hidden;
    background: var(--stage);
  }
  .sheet {
    position: relative; width: 1200px; height: 1000px;
  }
  .card {
    position: absolute; left: 290px; width: 620px; height: 401px;
    box-shadow: 0 6px 22px rgba(0,0,0,0.12);
    overflow: hidden;
  }
  /* Front */
  .card--front {
    top: 70px; background: var(--navy);
    display: flex; flex-direction: column; align-items: center; justify-content: center;
  }
  .brand-dot {
    width: 46px; height: 46px; border-radius: 50%;
    border: 2px solid var(--gold); margin-bottom: 26px;
  }
  .brand-name {
    font-family: "Cinzel", serif; font-weight: 500; color: var(--gold);
    text-align: center; line-height: 1.1;
  }
  .brand-name__main { display: block; font-size: 40px; letter-spacing: 1px; }
  .brand-name__sub { display: block; font-size: 20px; letter-spacing: 7px; margin-top: 6px; }

  /* Back */
  .card--back { top: 529px; background: var(--paper); }
  .card__band { position: absolute; inset: 0; }
  .contact {
    position: absolute; left: 52px; top: 84px;
    font-family: "Barlow Condensed", sans-serif; color: var(--ink);
  }
  .contact__name { font-size: 34px; font-weight: 600; letter-spacing: 0.5px; line-height: 1; }
  .contact__role { font-size: 19px; font-style: italic; font-weight: 300; color: #55546a; margin-top: 4px; }
  .contact__list { margin-top: 34px; display: grid; grid-template-columns: 92px auto; row-gap: 12px; }
  .contact__label { font-size: 19px; font-weight: 300; letter-spacing: 1.5px; color: var(--label-grey); text-transform: uppercase; }
  .contact__value { font-size: 20px; font-weight: 500; color: var(--ink); }
  .address {
    position: absolute; right: 26px; top: 120px; text-align: right;
    font-family: "Barlow Condensed", sans-serif; font-size: 15px; line-height: 1.55;
    color: var(--band-text); letter-spacing: 0.3px;
  }
  .address__company { font-style: italic; }
</style>
</head>
<body>
<main class="sheet">
  <section class="card card--front" aria-label="Business card front">
    <div class="brand-dot" aria-hidden="true"></div>
    <h1 class="brand-name">
      <span class="brand-name__main">FERNCASTLE</span>
      <span class="brand-name__sub">HOLDINGS</span>
    </h1>
  </section>

  <section class="card card--back" aria-label="Business card back">
    <svg class="card__band" width="620" height="401" viewBox="0 0 620 401" aria-hidden="true">
      <path d="M430 0 Q330 200 430 401 L620 401 L620 0 Z" fill="var(--navy-deep)"/>
      <path d="M430 0 Q330 200 430 401" fill="none" stroke="var(--gold)" stroke-width="5"/>
    </svg>
    <div class="contact">
      <p class="contact__name">JOHN DOE</p>
      <p class="contact__role">Your Position</p>
      <div class="contact__list">
        <span class="contact__label">Mobile</span><span class="contact__value">+44 20 79460018</span>
        <span class="contact__label">Email</span><span class="contact__value">johndoe@samplefirm.co.uk</span>
        <span class="contact__label">Website</span><span class="contact__value">samplefirm.co.uk</span>
      </div>
    </div>
    <address class="address">
      Ferncastle Holdings Limited<br>
      The Willows<br>
      Ashby Rise<br>
      Ashby, GL52 7TN<br>
      Company Number: 20418736<br>
      <span class="address__company">(Registered in England and Wales)</span>
    </address>
  </section>
</main>
</body>
</html>
```